Equine Rescue
Print Materials Design
Simple
Larkhollow Equine Sanctuary
2710 County Road 48B
Brackenridge NY 12790
TrotMeadow@fenmail.net
www.larkhollowequinesanctuaryinc.org
501(c)(3) Charity

```html
<!DOCTYPE html>
<html lang="en">
<head>
<meta charset="utf-8">
<title>Larkhollow Equine Sanctuary – Stationery</title>
<link rel="stylesheet" href="https://fonts.googleapis.com/css2?family=Arimo:wght@400;700&display=swap">
<style>
  :root {
    --brand-blue: #1f5db0;
    --paper: #ffffff;
    --stage: #ffffff;
    --frame-line: #e4e4e4;
    --edge: #d6d6d6;
    --shadow: rgba(0,0,0,0.18);
    --on-blue: #ffffff;
  }
  * { box-sizing: border-box; margin: 0; padding: 0; }
  html, body { width: 1200px; height: 681px; overflow: hidden; background: var(--stage); }
  body { font-family: "Arimo", Arial, sans-serif; color: var(--brand-blue); }

  .stage {
    position: relative; width: 1200px; height: 681px;
    border-bottom: 2px solid var(--frame-line);
  }
  .sheet {
    position: absolute; background: var(--paper);
    border: 1px solid var(--edge);
    box-shadow: 2px 3px 6px var(--shadow);
    overflow: hidden;
  }

  .brand { display: flex; align-items: center; gap: 8px; }
  .brand-dot { width: 22px; height: 22px; border-radius: 50%; background: var(--brand-blue); flex: none; }
  .brand-name { font-weight: 700; font-size: 15px; line-height: 1.1; color: var(--brand-blue); width: 130px; }

  .band {
    position: absolute; left: 0; right: 0; background: var(--brand-blue);
    color: var(--on-blue); font-size: 9px; line-height: 1.5; padding: 0 22px;
    display: flex; flex-direction: column; justify-content: center;
  }

  /* Envelope front */
  .envelope-front { left: 58px; top: 96px; width: 499px; height: 202px; }
  .envelope-front .brand { position: absolute; left: 18px; top: 14px; }
  .envelope-front .band { top: 160px; height: 24px; }

  /* Envelope back */
  .envelope-back { left: 58px; top: 324px; width: 499px; height: 209px; }
  .envelope-back .flap { position: absolute; left: 0; top: 0; }
  .envelope-back .seal { position: absolute; left: 240px; top: 44px; width: 18px; height: 18px; border-radius: 50%; background: var(--brand-blue); }

  /* Letterhead */
  .letterhead { left: 619px; top: 43px; width: 442px; height: 585px; }
  .letterhead .brand { position: absolute; left: 18px; top: 24px; }
  .letterhead .band { top: 519px; height: 44px; }

  /* Business card */
  .business-card {
    left: 970px; top: 163px; width: 146px; height: 70px;
    background: var(--brand-blue); border-color: var(--brand-blue);
  }
  .business-card .brand { position: absolute; left: 7px; top: 12px; gap: 3px; }
  .business-card .brand-dot { width: 8px; height: 8px; background: var(--on-blue); }
  .business-card .brand-name { color: var(--on-blue); font-size: 6.5px; width: 46px; }
  .card-details {
    position: absolute; right: 6px; top: 14px; width: 62px;
    color: var(--on-blue); font-size: 4.4px; line-height: 1.5;
    white-space: nowrap;
  }
</style>
</head>
<body>
<main class="stage">

  <section class="sheet envelope-front">
    <div class="brand">
      <span class="brand-dot"></span>
      <span class="brand-name">Larkhollow Equine Sanctuary</span>
    </div>
    <div class="band">2710 County Road 48B &nbsp;|&nbsp; Brackenridge NY 12790</div>
  </section>

  <section class="sheet envelope-back">
    <svg class="flap" width="499" height="209" viewBox="0 0 499 209" aria-hidden="true">
      <path d="M2 2 L20 34 Q26 42 38 42 L461 42 Q473 42 479 34 L497 2" fill="none" stroke="#9a9a9a" stroke-width="1.2"/>
    </svg>
    <span class="seal"></span>
  </section>

  <section class="sheet letterhead">
    <div class="brand">
      <span class="brand-dot"></span>
      <span class="brand-name">Larkhollow Equine Sanctuary</span>
    </div>
    <div class="band">
      <span>2710 County Road 48B &nbsp;|&nbsp; Brackenridge NY 12790</span>
      <span>Phone: (845) 555-0174 &nbsp;|&nbsp; Fax: (845) 555-0198 &nbsp;|&nbsp; www.larkhollowequinesanctuaryinc.org</span>
    </div>
  </section>

  <section class="sheet business-card">
    <div class="brand">
      <span class="brand-dot"></span>
      <span class="brand-name">Larkhollow Equine Sanctuary</span>
    </div>
    <div class="card-details">
      2710 County Road 48B<br>
      Brackenridge NY 12790<br>
      (845) 555-0174<br>
      TrotMeadow@fenmail.net<br>
      501(c)(3) Charity
    </div>
  </section>

</main>
</body>
</html>
```